Strong, modern, clean Business Card design

Looking for a stunning, but CLEAN business card design. While we are a faith-based organization, we do NOT want this to look religious.

Industry/Entity Type

Non-Profit

Contact Information for Business Card

Dale Munroe | Lead Pastor
dale@BrightHarvestHope.org
970-555-0148
PO Box 7316
Loveland, CO 80571

Font styles to use
Serif
Sans Serif

Requirements
Should not have
• Religious imagery or symbolism

```html
<!DOCTYPE html>
<html lang="en">
<head>
<meta charset="utf-8">
<title>Bright Harvest Church – Business Card</title>
<link rel="stylesheet" href="https://fonts.googleapis.com/css2?family=Libre+Baskerville:wght@400;700&family=Lato:wght@400&display=swap">
<style>
  :root {
    --page-bg: #e9e6e3;
    --card-bg: #161616;
    --accent: #4d7d97;
    --text-light: #d6d6d6;
  }
  * { margin: 0; padding: 0; box-sizing: border-box; }
  html, body {
    width: 1200px;
    height: 900px;
    overflow: hidden;
    background: var(--page-bg);
  }
  .canvas {
    position: relative;
    width: 1200px;
    height: 900px;
  }
  .business-card {
    position: absolute;
    left: 274px;
    top: 248px;
    width: 652px;
    height: 405px;
    background: var(--card-bg);
    border-radius: 203px 0 0 203px;
    box-shadow: 0 10px 30px rgba(0,0,0,0.18);
  }
  .brand {
    position: absolute;
    left: 52px;
    top: 82px;
    width: 318px;
    text-align: center;
  }
  .brand-mark {
    display: block;
    width: 108px;
    height: 108px;
    margin: 0 auto;
    background: var(--accent);
    border-radius: 14px;
  }
  .brand-name {
    margin-top: 26px;
    font-family: "Libre Baskerville", Georgia, serif;
    font-weight: 400;
    color: var(--accent);
    text-transform: uppercase;
    line-height: 1.15;
  }
  .brand-name .line-main {
    display: block;
    font-size: 29px;
    letter-spacing: 1px;
  }
  .brand-name .line-sub {
    display: block;
    font-size: 19px;
    letter-spacing: 15px;
    margin-top: 6px;
    padding-left: 15px;
  }
  .contact {
    position: absolute;
    right: 46px;
    top: 60px;
    text-align: right;
    font-family: "Lato", Arial, sans-serif;
    color: var(--text-light);
    font-size: 17px;
    line-height: 23px;
  }
  .person-name {
    font-family: "Libre Baskerville", Georgia, serif;
    font-weight: 700;
    font-size: 20px;
    color: var(--accent);
    text-transform: uppercase;
    letter-spacing: 0.3px;
    line-height: 26px;
  }
  .address { margin-top: 117px; }
  .reach { margin-top: 28px; }
  .reach-line {
    display: flex;
    justify-content: flex-end;
    align-items: center;
    gap: 5px;
    height: 24px;
  }
  .reach-icon { width: 14px; height: 14px; fill: var(--accent); }
</style>
</head>
<body>
<main class="canvas">
  <section class="business-card">
    <div class="brand">
      <span class="brand-mark"></span>
      <p class="brand-name">
        <span class="line-main">Bright Harvest</span>
        <span class="line-sub">Church</span>
      </p>
    </div>

    <div class="contact">
      <p class="person-name">Dale Munroe</p>
      <p class="role">Lead Pastor</p>

      <p class="address">PO Box 7316<br>Loveland, CO 80571</p>

      <div class="reach">
        <p class="reach-line">970-555-0148
          <svg class="reach-icon" viewBox="0 0 16 16" aria-hidden="true">
            <path d="M2 6c0-2 2.5-3.5 6-3.5S14 4 14 6l-3 .6-.6-1.6H5.6L5 6.6z"/>
            <path d="M4 8h8l1.5 5h-11z"/>
          </svg>
        </p>
        <p class="reach-line">dale@BrightHarvestHope.org
          <svg class="reach-icon" viewBox="0 0 16 16" aria-hidden="true">
            <path d="M1 3h14v10H1z M2 4.2v.3l6 4.3 6-4.3v-.3z" fill-rule="evenodd"/>
          </svg>
        </p>
      </div>
    </div>
  </section>
</main>
</body>
</html>
```